TrellisMark needs banners for publishing in CloudVerve Bazaar Hub

1. A banner of the size 1200 x 300
2. A tile image of the size 280 x 205

My company is: www.trellismark-demo.com. I need the above files for placing it on CloudVerve BazaarHub. Please see the following links to know exactly where these files will need to be placed:

https://bazaarhub.cloudverve-demo.com/results?keywords=TrellisMark - This is where the Tile Image will go.

https://bazaarhub.cloudverve-demo.com/listingDetail?listingId=k7R5000000M2QTyWBD - This is where the Banner Image will go.

Please see examples of what CloudVerve as good Tile Images and Banner Images:
For Tile Image: https://bazaarhub.cloudverve-demo.com/

For Banner Image: https://bazaarhub.cloudverve-demo.com/listingDetail?listingId=k7R50000009bvZ8WBL

Target Market(s)

Manufacturing Industry

Industry/Entity Type

It Company

Colors
33a6d7
cee9f5

```html
<!DOCTYPE html>
<html lang="en">
<head>
<meta charset="utf-8">
<title>TrellisMark – CloudVerve BazaarHub Banners</title>
<link rel="stylesheet" href="https://fonts.googleapis.com/css2?family=Oswald:wght@300;400&family=Open+Sans:wght@400&display=swap">
<style>
  :root {
    --brand-blue: #33a6d7;
    --brand-light: #cee9f5;
    --ink-dark: #1f2a33;
    --button-dark: #3b3b3d;
    --arc-gray: #8e8f91;
    --backdrop: #2a150d;
    --white: #ffffff;
    --photo-warm: #b9a58a;
    --photo-cool: #d8d2c8;
  }
  * { margin: 0; padding: 0; box-sizing: border-box; }
  html, body {
    width: 1200px; height: 761px; overflow: hidden;
    background: var(--backdrop);
  }
  .board {
    position: absolute; left: 0; top: 0;
    width: 1360px; height: 862px;
    transform: scale(0.88235); transform-origin: 0 0;
  }
  .banner, .tile {
    position: absolute; overflow: hidden;
    background: var(--brand-blue);
    font-family: "Oswald", sans-serif;
  }
  .banner { left: 63px; top: 134px; width: 1200px; height: 300px; }
  .tile { left: 64px; top: 467px; width: 279px; height: 204px; outline: 1px solid #111; }
  .art { position: absolute; inset: 0; }
  .logo-plate {
    position: absolute; background: var(--white);
    display: flex; align-items: center; justify-content: center;
  }
  .banner .logo-plate { left: 154px; top: 0; width: 337px; height: 67px; gap: 12px; }
  .tile .logo-plate { left: 0; top: 0; width: 155px; height: 37px; gap: 7px; }
  .logo-dot { border-radius: 50%; background: var(--brand-blue); }
  .banner .logo-dot { width: 34px; height: 34px; }
  .tile .logo-dot { width: 20px; height: 20px; }
  .logo-name { font-family: "Oswald", sans-serif; font-weight: 400; color: var(--brand-blue); letter-spacing: 0.5px; }
  .banner .logo-name { font-size: 28px; }
  .tile .logo-name { font-size: 16px; }
  .headline { position: absolute; color: var(--white); font-weight: 300; text-align: center; line-height: 1; }
  .banner .headline { left: 20px; width: 598px; top: 86px; font-size: 48px; }
  .tile .headline { left: 0; width: 140px; top: 48px; font-size: 17px; line-height: 1.1; font-weight: 400; }
  .subline { position: absolute; color: var(--ink-dark); text-align: center; font-weight: 400; }
  .banner .subline { left: 20px; width: 598px; top: 138px; font-size: 22px; }
  .tile .subline { left: 8px; width: 124px; top: 94px; font-size: 12.5px; line-height: 1.2; }
  .benefits {
    position: absolute; left: 44px; top: 184px; width: 560px;
    display: flex; justify-content: space-between; list-style: none;
    color: var(--white); font-size: 19px; font-weight: 300;
    border-bottom: 1px solid rgba(255,255,255,0.25); padding-bottom: 8px;
  }
  .benefits li { display: flex; align-items: center; gap: 6px; }
  .benefits svg { width: 20px; height: 14px; }
  .cta {
    position: absolute; background: var(--button-dark); color: var(--white);
    font-family: "Open Sans", sans-serif; display: flex; align-items: center; justify-content: center;
  }
  .banner .cta { left: 203px; top: 240px; width: 242px; height: 41px; font-size: 19px; }
  .tile .cta { left: 12px; top: 168px; width: 125px; height: 26px; font-size: 10.5px; }
</style>
</head>
<body>
<div class="board">

  <section class="banner">
    <svg class="art" width="1200" height="300" viewBox="0 0 1200 300">
      <defs>
        <linearGradient id="photoTone" x1="0" y1="0" x2="1" y2="1">
          <stop offset="0" stop-color="var(--photo-cool)"/>
          <stop offset="1" stop-color="var(--photo-warm)"/>
        </linearGradient>
      </defs>
      <rect x="1040" y="0" width="160" height="300" fill="var(--brand-light)"/>
      <ellipse cx="885" cy="140" rx="255" ry="262" fill="var(--arc-gray)"/>
      <ellipse cx="878" cy="140" rx="243" ry="250" fill="url(#photoTone)" role="img" aria-label="Photo: warehouse staff reviewing a clipboard among packed boxes"/>
    </svg>
    <div class="logo-plate"><span class="logo-dot"></span><span class="logo-name">TRELLISMARK</span></div>
    <h1 class="headline">ANYTIME. ANYWHERE. ANYPLACE</h1>
    <p class="subline">Built On The World's Most Scalable, Secure Enterprise Cloud Platform</p>
    <ul class="benefits">
      <li><svg viewBox="0 0 20 14"><path d="M0 0 L20 7 L0 14 L5 7 Z" fill="#1b6fa3"/></svg>1st Thought Leadership</li>
      <li><svg viewBox="0 0 20 14"><path d="M0 0 L20 7 L0 14 L5 7 Z" fill="#1b6fa3"/></svg>100+ Years of Experience</li>
      <li><svg viewBox="0 0 20 14"><path d="M0 0 L20 7 L0 14 L5 7 Z" fill="#1b6fa3"/></svg>100% Entrepreneurs</li>
    </ul>
    <div class="cta">GET STARTED NOW</div>
  </section>

  <section class="tile">
    <svg class="art" width="279" height="204" viewBox="0 0 279 204">
      <defs>
        <linearGradient id="tileTone" x1="0" y1="0" x2="1" y2="1">
          <stop offset="0" stop-color="var(--photo-cool)"/>
          <stop offset="1" stop-color="var(--photo-warm)"/>
        </linearGradient>
      </defs>
      <rect x="150" y="0" width="129" height="204" fill="var(--brand-light)"/>
      <ellipse cx="258" cy="110" rx="126" ry="150" fill="var(--arc-gray)"/>
      <ellipse cx="262" cy="110" rx="120" ry="146" fill="url(#tileTone)" role="img" aria-label="Photo: two warehouse staff checking a clipboard"/>
    </svg>
    <div class="logo-plate"><span class="logo-dot"></span><span class="logo-name">TRELLISMARK</span></div>
    <h2 class="headline">ANYTIME. ANYWHERE.<br>ANYPLACE</h2>
    <p class="subline">Built On The World's Most Scalable, Secure Enterprise Cloud Platform</p>
    <div class="cta">GET STARTED NOW</div>
  </section>

</div>
</body>
</html>
```